International game business needs app design

We are planning to release a new mobile game on Qbe5 which requires a fresh, flat, reduced and functional design, fulfilling Brindle’s Qbe5 design guidelines
.
The design shall be created for a dashboard, where players should be able to pick levels (icon + short description; 300+ levels), opponents (icon/photo/avatar image + short description; 5-100) and read/delete system/chat messages (icon, 2-3 actions (delete, accept/decline), text with up to 500 characters; 1-100 entries), Menu bar (settings, shop, leaderboards, achievements, and one or two more menu items) It must consider means to search/select levels and opponents. Would be nice to have an option to start playing immediately (with a random opponent on a random level)

Overall Style/Look: fresh, flat, functional, lot’s of free space, warm color scheme. If full screen images are being used it must be considered that there are user-generated photos or avatars which have to work with it in combination

Ideally the design is responsive and would work both on a smartphone and a tablet. Smartphone is top priority, tablet is optional.

The app will be a game for women predominantly, aged 25-35, with higher education and household net income, which should be reflected in color scheme, icons and navigation.

Some of us like flat design, so you might stick to that or impress all of us with something completely new!

The winner will have the chance to design all screens for the app and will have access to a much bigger budget.

UPDATE: A wireframe is attached - but you don't have to follow the depicted layout. Actually it would be highly appreciated if you could come up with something new. The only important thing is that all the listed components must appear somehow on the dashboard.

Target Market(s)

US, AU, NZ, GB, CA

Industry/Entity Type

Education

Colors

Designer to choose colors to be used in the design.

Requirements
Must have
• All the functional components described above.
Design must be in line with Qbe5 design guidelines https://makers.brindlehub.example/library/qbe/documentation/UserExperience/Conceptual/TouchGuide/index.html
Nice to have
• We would like to have someone with the following attributes:
* minimum 5 qbe design in your past at least 2 of them responsive – please provide links to the apps you created
* besides UI designer skills would be nice you to have UX skills

The most important factors for us are quality, creativity, speed, flexibility (“be able to take criticism into account”)
Should not have
• We don’t want a girly design so please don’t use too much pinks, flowers and such. The design should be acceptable by men too.

```html
<!DOCTYPE html>
<html lang="en">
<head>
<meta charset="utf-8">
<title>Game Dashboard</title>
<link rel="stylesheet" href="https://fonts.googleapis.com/css2?family=Open+Sans:wght@400;600;700&display=swap">
<style>
  :root{
    --page:#e4e4e4;
    --navy:#393660;
    --navy-dark:#2f2c52;
    --pink:#d9415f;
    --screen:#f2f2f2;
    --card:#ffffff;
    --bar:#c8c8c8;
    --bar-text:#ffffff;
    --text:#333333;
    --muted:#9a9a9a;
    --green:#5cb85c;
  }
  *{box-sizing:border-box;margin:0;padding:0}
  html,body{width:1200px;height:897px;overflow:hidden}
  body{background:var(--page);font-family:"Open Sans",Arial,sans-serif;color:var(--text);position:relative}
  .screen{position:absolute;left:375px;top:40px;width:450px;height:817px;background:var(--screen);overflow:hidden;box-shadow:0 10px 40px rgba(0,0,0,.15)}
  .status-bar{height:28px;background:var(--navy);color:#fff;font-size:13px;font-weight:600;display:flex;align-items:center;justify-content:space-between;padding:0 12px}
  .status-bar .carrier{display:flex;align-items:center;gap:6px}
  .status-bar .battery{display:flex;align-items:center;gap:6px}
  .nav-bar{height:60px;background:var(--navy);display:flex}
  .nav-item{flex:1;display:flex;align-items:center;justify-content:center}
  .nav-item.active{background:var(--navy-dark)}
  .level-path{position:relative;height:74px;background:var(--screen)}
  .level-path svg{position:absolute;left:0;top:0}
  .search{margin:0 14px 10px;height:40px;background:var(--card);border-radius:3px;display:flex;align-items:center;justify-content:space-between;padding:0 14px;color:var(--muted);font-size:14px}
  .opponent{background:var(--card);margin:0 0 0}
  .opponent-body{display:flex;padding:14px 18px 12px;gap:20px;align-items:flex-start}
  .avatar{width:108px;height:108px;border-radius:50%;flex:none}
  .avatar.sophia{background:linear-gradient(135deg,#c9a088,#6b4a37)}
  .avatar.angie{background:linear-gradient(135deg,#8e8a84,#3a3230)}
  .opponent-name{font-size:19px;font-weight:600;margin:16px 0 8px}
  .opponent-bio{font-size:11px;line-height:1.5;color:var(--muted)}
  .actions{display:flex;background:var(--bar);color:var(--bar-text);font-size:12px;height:36px}
  .action{flex:1;display:flex;align-items:center;justify-content:center;gap:8px;border-right:1px solid #d8d8d8}
  .action:last-child{border-right:none}
  .lower{display:flex;gap:10px;padding:12px 10px 0}
  .message,.invite{background:var(--card);flex:1;height:170px;position:relative;padding:12px}
  .close{position:absolute;right:8px;top:8px;width:16px;height:16px;background:var(--bar);color:#fff;font-size:11px;line-height:16px;text-align:center}
  .message-head{display:flex;gap:10px;align-items:center;margin-bottom:10px}
  .mini-avatar{width:40px;height:40px;border-radius:50%;background:linear-gradient(135deg,#d8a585,#8a5a3e)}
  .message-label{font-size:10px;color:var(--pink)}
  .message-from{font-size:13px;font-weight:600}
  .message-text{font-size:11px;line-height:1.5;color:var(--muted)}
  .invite{padding:0}
  .game-art{height:100px;background:linear-gradient(160deg,#6cc0e8,#7cb04a 60%,#c98a3a)}
  .invite-text{font-size:11px;line-height:1.45;color:var(--muted);padding:8px 12px;padding-right:50px}
  .invite-text b{color:var(--pink);font-weight:400}
  .invite-buttons{position:absolute;right:10px;bottom:12px;display:flex;gap:6px}
  .play-button{position:absolute;left:10px;right:10px;bottom:16px;height:64px;background:var(--pink);color:#fff;font-size:21px;font-weight:600;display:flex;align-items:center;justify-content:center}
</style>
</head>
<body>
<main class="screen">
  <div class="status-bar">
    <span class="carrier">
      <svg width="22" height="10" viewBox="0 0 22 10"><rect x="0" y="7" width="3" height="3" fill="#fff"/><rect x="4" y="5" width="3" height="5" fill="#fff"/><rect x="8" y="3" width="3" height="7" fill="#fff"/><rect x="12" y="1" width="3" height="9" fill="#fff"/><rect x="16" y="0" width="3" height="10" fill="#fff"/></svg>
      DINE
    </span>
    <span>10:35 AM</span>
    <span class="battery">
      <svg width="12" height="12" viewBox="0 0 12 12"><circle cx="6" cy="6" r="5.5" fill="#fff"/><path d="M6 2.5V6h3" stroke="#393660" stroke-width="1.4" fill="none"/></svg>
      65%
      <svg width="26" height="12" viewBox="0 0 26 12"><rect x="0.5" y="0.5" width="22" height="11" fill="none" stroke="#fff"/><rect x="2" y="2" width="13" height="8" fill="#fff"/><rect x="23" y="4" width="2" height="4" fill="#fff"/></svg>
    </span>
  </div>

  <nav class="nav-bar">
    <div class="nav-item" aria-label="settings">
      <svg width="22" height="22" viewBox="0 0 24 24" fill="none" stroke="#8c89b8" stroke-width="2"><circle cx="12" cy="12" r="3.5"/><path d="M12 2v3M12 19v3M2 12h3M19 12h3M4.9 4.9l2.1 2.1M17 17l2.1 2.1M4.9 19.1L7 17M17 7l2.1-2.1"/></svg>
    </div>
    <div class="nav-item" aria-label="shop">
      <svg width="24" height="22" viewBox="0 0 24 22" fill="none" stroke="#8c89b8" stroke-width="2"><path d="M1 2h4l3 12h12l3-9H7"/><circle cx="9" cy="19" r="1.6"/><circle cx="18" cy="19" r="1.6"/></svg>
    </div>
    <div class="nav-item active" aria-label="leaderboards">
      <svg width="20" height="22" viewBox="0 0 20 22" fill="none" stroke="#8c89b8" stroke-width="2"><rect x="2" y="1" width="16" height="20" rx="1"/><path d="M6 7h8M6 11h8M6 15h5"/></svg>
    </div>
    <div class="nav-item" aria-label="achievements">
      <svg width="24" height="24" viewBox="0 0 24 24" fill="none" stroke="#8c89b8" stroke-width="2"><circle cx="12" cy="12" r="4"/><path d="M12 1v4M12 19v4M1 12h4M19 12h4M4 4l3 3M17 17l3 3M4 20l3-3M17 7l3-3"/></svg>
    </div>
  </nav>

  <section class="level-path" aria-label="level selection">
    <svg width="450" height="74" viewBox="0 0 450 74" font-family="Open Sans, Arial, sans-serif">
      <line x1="0" y1="36" x2="150" y2="36" stroke="#d9415f" stroke-width="3"/>
      <line x1="150" y1="36" x2="450" y2="36" stroke="#393660" stroke-width="3"/>
      <g text-anchor="middle" fill="#fff">
        <circle cx="36" cy="36" r="19" fill="#d9415f" stroke="#f2f2f2" stroke-width="3"/>
        <text x="36" y="38" font-size="15" font-weight="700">1</text><text x="36" y="48" font-size="6">level</text>
        <circle cx="105" cy="36" r="19" fill="#d9415f" stroke="#f2f2f2" stroke-width="3"/>
        <text x="105" y="38" font-size="15" font-weight="700">2</text><text x="105" y="48" font-size="6">level</text>
        <circle cx="174" cy="36" r="19" fill="#393660" stroke="#f2f2f2" stroke-width="3"/>
        <text x="174" y="38" font-size="15" font-weight="700">3</text><text x="174" y="48" font-size="6">level</text>
        <circle cx="243" cy="36" r="19" fill="#393660" stroke="#f2f2f2" stroke-width="3"/>
        <text x="243" y="38" font-size="15" font-weight="700">4</text><text x="243" y="48" font-size="6">level</text>
        <circle cx="312" cy="36" r="19" fill="#393660" stroke="#f2f2f2" stroke-width="3"/>
        <text x="312" y="38" font-size="15" font-weight="700">5</text><text x="312" y="48" font-size="6">level</text>
        <circle cx="381" cy="36" r="19" fill="#393660" stroke="#f2f2f2" stroke-width="3"/>
        <text x="381" y="38" font-size="15" font-weight="700">6</text><text x="381" y="48" font-size="6">level</text>
      </g>
    </svg>
  </section>

  <div class="search">
    <span>search opponent</span>
    <svg width="16" height="16" viewBox="0 0 16 16" fill="none" stroke="#bbb" stroke-width="1.6"><circle cx="6.5" cy="6.5" r="5"/><path d="M10.5 10.5L15 15"/></svg>
  </div>

  <article class="opponent">
    <div class="opponent-body">
      <div class="avatar sophia" role="img" aria-label="profile photo of opponent"></div>
      <div>
        <h2 class="opponent-name">Sophia Price</h2>
        <p class="opponent-bio">Loves word puzzles and quick rounds after work. Always up for a friendly rematch on weekends.</p>
      </div>
    </div>
    <div class="actions">
      <span class="action"><svg width="14" height="14" viewBox="0 0 24 24" fill="#fff"><path d="M12 1l3.4 7 7.6 1-5.5 5.3 1.3 7.7L12 18.3 5.2 22l1.3-7.7L1 9l7.6-1z"/></svg>level 18</span>
      <span class="action"><svg width="14" height="13" viewBox="0 0 24 22" fill="#fff"><path d="M12 21L2.5 11.5A5.8 5.8 0 0112 3.6a5.8 5.8 0 019.5 7.9z"/></svg>add as friend</span>
      <span class="action"><svg width="15" height="13" viewBox="0 0 24 20" fill="#fff"><path d="M2 1h20v13H9l-5 5v-5H2z"/></svg>chat</span>
    </div>
  </article>

  <article class="opponent">
    <div class="opponent-body">
      <div class="avatar angie" role="img" aria-label="profile photo of opponent"></div>
      <div>
        <h2 class="opponent-name">Angie x</h2>
        <p class="opponent-bio">Strategy fan climbing the ranks. Challenge me to any level above ten and bring your best moves.</p>
      </div>
    </div>
    <div class="actions">
      <span class="action"><svg width="14" height="14" viewBox="0 0 24 24" fill="#fff"><path d="M12 1l3.4 7 7.6 1-5.5 5.3 1.3 7.7L12 18.3 5.2 22l1.3-7.7L1 9l7.6-1z"/></svg>level 21</span>
      <span class="action"><svg width="14" height="13" viewBox="0 0 24 22" fill="#fff"><path d="M12 21L2.5 11.5A5.8 5.8 0 0112 3.6a5.8 5.8 0 019.5 7.9z"/></svg>add as friend</span>
      <span class="action"><svg width="15" height="13" viewBox="0 0 24 20" fill="#fff"><path d="M2 1h20v13H9l-5 5v-5H2z"/></svg>chat</span>
    </div>
  </article>

  <section class="lower">
    <article class="message">
      <span class="close">×</span>
      <div class="message-head">
        <div class="mini-avatar" role="img" aria-label="sender profile photo"></div>
        <div>
          <p class="message-label">message from</p>
          <p class="message-from">Alex Robson</p>
        </div>
      </div>
      <p class="message-text">Great match yesterday! Want to try level nine together tonight? I think we can beat it.</p>
    </article>
    <article class="invite">
      <div class="game-art" role="img" aria-label="fantasy strategy game cover art"></div>
      <span class="close">×</span>
      <p class="invite-text">Your friend <b>Amanda</b> just played a game. Wanna try it too?</p>
      <div class="invite-buttons">
        <svg width="18" height="18" viewBox="0 0 18 18" aria-label="accept"><circle cx="9" cy="9" r="9" fill="#5cb85c"/><path d="M5 9.5l2.5 2.5L13 6.5" stroke="#fff" stroke-width="2" fill="none"/></svg>
        <svg width="18" height="18" viewBox="0 0 18 18" aria-label="decline"><circle cx="9" cy="9" r="9" fill="#d9415f"/><path d="M6 6l6 6M12 6l-6 6" stroke="#fff" stroke-width="2"/></svg>
      </div>
    </article>
  </section>

  <a class="play-button">Play a random game</a>
</main>
</body>
</html>
```